KORBLE Development is an idea development firm. This business card is for Weekend Wicket League, a site that allows users from all over the world to play fantasy cricket against each other.
We need a business card for WWL using our logo and its associated colors. The cards are for the two founders, Tobias Whitlow and Martin Dobrescu. We would like our own cards.
We are handing our card to potential investors and sponsors of our site. It needs to be unique (like our brand.)
Updates
I wanted to thank everyone for their awesome designs!!! It was a hard choice - we narrowed it down to 7 then to three then to 1. All of you are extremely talented - THANK YOU.
Target Market(s)
Potential Investors, Partners
Industry/Entity Type
Business
Contact Information for Business Card
Korble Development : Weekend Wicket League
Tobias Whitlow
Founder
555-204-7316
tobias@korble.example
www.weekendwicketleague.example
....
Martin Dobrescu
Founder
555-871-0492
martin@korble.example
Look and feel

```html
<!DOCTYPE html>
<html lang="en">
<head>
<meta charset="utf-8">
<title>Weekend Wicket League — Business Card</title>
<link href="https://fonts.googleapis.com/css2?family=Josefin+Sans:wght@300;400&display=swap" rel="stylesheet">
<style>
  :root {
    --card-green: #2f7a36;
    --accent-lime: #a6c83a;
    --backdrop: #ecebe5;
    --logo-white: #ffffff;
  }
  html, body {
    margin: 0;
    padding: 0;
    width: 1200px;
    height: 900px;
    overflow: hidden;
    background: var(--backdrop);
  }
  .canvas {
    position: relative;
    width: 1200px;
    height: 900px;
    font-family: "Josefin Sans", "Century Gothic", sans-serif;
  }
  .card {
    position: absolute;
    left: 250px;
    width: 700px;
    height: 400px;
    background: var(--card-green);
    overflow: hidden;
    box-shadow: 0 6px 18px rgba(0,0,0,0.18);
  }
  .card--front { top: 35px; }
  .card--back { top: 465px; }
  .card__shapes {
    position: absolute;
    inset: 0;
    width: 700px;
    height: 400px;
  }

  /* Front: brand lockup */
  .brand {
    position: absolute;
    top: 70px;
    left: 0;
    width: 700px;
    display: flex;
    justify-content: center;
    align-items: center;
    gap: 14px;
  }
  .brand__dot {
    width: 34px;
    height: 34px;
    border-radius: 50%;
    background: var(--accent-lime);
  }
  .brand__name {
    color: var(--logo-white);
    font-weight: 400;
    font-size: 22px;
    line-height: 1.2;
    text-align: center;
  }

  /* Back: name & contacts */
  .holder-name {
    position: absolute;
    right: 105px;
    top: 42px;
    margin: 0;
    color: var(--accent-lime);
    font-weight: 300;
    font-size: 80px;
    line-height: 0.95;
    letter-spacing: 2px;
    text-align: right;
    text-transform: uppercase;
  }
  .contact-row {
    position: absolute;
    left: 24px;
    right: 24px;
    display: flex;
    align-items: center;
    gap: 10px;
    color: var(--accent-lime);
    font-weight: 300;
    font-size: 18px;
    white-space: nowrap;
  }
  .contact-row__rule {
    flex: 1;
    height: 2px;
    background: var(--accent-lime);
  }
  .contact-row--company { top: 282px; }
  .contact-row--phone { top: 322px; }
</style>
</head>
<body>
<main class="canvas">

  <section class="card card--front" aria-label="Card front">
    <svg class="card__shapes" viewBox="0 0 700 400" aria-hidden="true">
      <rect x="0" y="236" width="700" height="9" fill="var(--accent-lime)"/>
      <circle cx="0" cy="240" r="62" fill="var(--accent-lime)"/>
      <circle cx="350" cy="240" r="30" fill="var(--accent-lime)"/>
      <circle cx="700" cy="240" r="62" fill="var(--accent-lime)"/>
    </svg>
    <div class="brand">
      <span class="brand__dot"></span>
      <span class="brand__name">Weekend Wicket<br>League</span>
    </div>
  </section>

  <section class="card card--back" aria-label="Card back">
    <svg class="card__shapes" viewBox="0 0 700 400" aria-hidden="true">
      <circle cx="700" cy="70" r="80" fill="var(--accent-lime)"/>
      <rect x="0" y="262" width="700" height="4" fill="var(--accent-lime)"/>
      <circle cx="30" cy="195" r="65" fill="var(--accent-lime)"/>
      <rect x="0" y="380" width="700" height="2" fill="var(--accent-lime)"/>
    </svg>
    <h1 class="holder-name">Tobias<br>Whitlow</h1>
    <div class="contact-row contact-row--company">
      <span>Korble Development : Weekend Wicket League</span>
      <span class="contact-row__rule"></span>
      <span>tobias@korble.example</span>
    </div>
    <div class="contact-row contact-row--phone">
      <span>555-204-7316</span>
      <span class="contact-row__rule"></span>
      <span>www.weekendwicketleague.example</span>
    </div>
  </section>

</main>
</body>
</html>
```